Clean and modern business cards

Looking for an updated business card design for my dental office “corvanta dental” . Looking for a modern clean / sleek design . I’m thinking black background but open to seeing other options . One side needs to have an appointment card . Card needs to have logo, dentist name , phone, email , address . I’ve attached couple of cards I thought were cool as well as my logo
Target Market(s)
Dental patients
Industry/Entity Type
Dentistry
Contact Information for Business Card
Phone email address

```html
<!DOCTYPE html>
<html lang="en">
<head>
<meta charset="utf-8">
<title>Corvanta Dental – Business Card</title>
<link href="https://fonts.googleapis.com/css2?family=Heebo:wght@400;500;700;800&display=swap" rel="stylesheet">
<style>
  :root {
    --backdrop: #e4d9a6;
    --card: #1e1e1f;
    --white: #f4f4f4;
    --green: #8cc63f;
    --teal: #2fa6bb;
    --yellow: #fcd338;
    --purple: #7a3aa8;
    --red: #ea4324;
    --blue: #2f4fb4;
  }
  * { box-sizing: border-box; margin: 0; padding: 0; }
  html, body {
    width: 1200px; height: 1030px; overflow: hidden;
    background: var(--backdrop);
    font-family: "Heebo", Arial, sans-serif;
  }
  .card {
    position: absolute; top: 129px;
    width: 418px; height: 729px;
    background: var(--card);
  }
  .card--front { left: 168px; }
  .card--back { left: 624px; }

  .brand-art {
    position: absolute; border-radius: 50%;
    background:
      radial-gradient(circle at 30% 30%, rgba(252,211,56,.85), transparent 45%),
      radial-gradient(circle at 72% 35%, rgba(47,166,187,.85), transparent 45%),
      radial-gradient(circle at 35% 75%, rgba(122,58,168,.85), transparent 45%),
      radial-gradient(circle at 70% 72%, rgba(234,67,36,.8), transparent 45%),
      radial-gradient(circle at 50% 50%, rgba(140,198,63,.9), rgba(47,79,180,.6) 70%, transparent 72%);
  }
  .card--front .brand-art { left: 66px; top: 186px; width: 290px; height: 260px; }
  .card--back .brand-art { left: 86px; top: 106px; width: 250px; height: 218px; }

  .dentist-name {
    position: absolute; right: 56px; top: 571px;
    color: var(--green); font-size: 15px; font-weight: 500; letter-spacing: .02em;
  }
  .wordmark {
    position: absolute; right: 56px; top: 592px;
    color: var(--white); font-weight: 800; text-align: right; line-height: 1;
  }
  .wordmark__name { display: block; font-size: 50px; letter-spacing: .005em; }
  .wordmark__sub { display: block; font-size: 20px; letter-spacing: .42em; margin-top: 10px; margin-right: -.42em; }

  .appointment { position: absolute; left: 0; top: 381px; width: 100%; }
  .appointment__title {
    position: absolute; left: 115px; top: 0; width: 256px; height: 31px;
    border-radius: 16px; background: var(--yellow);
    color: #1e1e1f; font-size: 14px; font-weight: 700;
    display: flex; align-items: center; justify-content: center;
  }
  .field { position: absolute; left: 0; width: 100%; height: 31px; }
  .field--date { top: 36px; }
  .field--time { top: 72px; }
  .field__label {
    position: absolute; left: 50px; top: 4px; font-size: 18px; font-weight: 400;
  }
  .field--date .field__label { color: var(--green); }
  .field--time .field__label { color: var(--teal); }
  .field__line {
    position: absolute; left: 115px; top: 0; width: 256px; height: 31px;
    border-radius: 16px; background: var(--white);
  }
  .policy {
    position: absolute; left: 52px; top: 111px; width: 330px;
    color: var(--yellow); font-size: 14px; line-height: 18px;
  }

  .contact {
    position: absolute; left: 0; top: 580px; width: 100%;
    text-align: center; font-size: 13px; list-style: none;
  }
  .contact li { height: 26px; display: flex; align-items: center; justify-content: center; gap: 7px; }
  .contact svg { width: 13px; height: 13px; }
  .contact__web { color: var(--yellow); }
  .contact__phone { color: var(--teal); }
  .contact__email { color: var(--green); }
  .contact__address { color: var(--white); letter-spacing: .02em; margin-top: 2px; }
</style>
</head>
<body>
  <section class="card card--front">
    <div class="brand-art" role="img" aria-label="Clinic logo symbol: tooth surrounded by colourful bubbles"></div>
    <p class="dentist-name">Dr. ELENA VARSHO</p>
    <h1 class="wordmark">
      <span class="wordmark__name">CORVANTA</span>
      <span class="wordmark__sub">DENTAL</span>
    </h1>
  </section>

  <section class="card card--back">
    <div class="brand-art" role="img" aria-label="Clinic logo symbol: tooth surrounded by colourful bubbles"></div>
    <div class="appointment">
      <p class="appointment__title">YOUR NEXT APPOINTMENT IS:</p>
      <div class="field field--date"><span class="field__label">DATE</span><span class="field__line"></span></div>
      <div class="field field--time"><span class="field__label">TIME</span><span class="field__line"></span></div>
      <p class="policy">To cancel or reshedule please notify us at least 48 hours prior to your scheduled appointment.</p>
    </div>
    <ul class="contact">
      <li class="contact__web">
        <svg viewBox="0 0 14 14"><circle cx="7" cy="7" r="7" fill="var(--yellow)"/><circle cx="7" cy="7" r="4" fill="none" stroke="#1e1e1f" stroke-width="1.2"/><path d="M3 7h8M7 3v8" stroke="#1e1e1f" stroke-width="1"/></svg>
        www.corvantadental.ca
      </li>
      <li class="contact__phone">
        <svg viewBox="0 0 14 14"><circle cx="7" cy="7" r="7" fill="var(--teal)"/><rect x="4.8" y="3.2" width="4.4" height="7.6" rx="1" fill="none" stroke="#1e1e1f" stroke-width="1.2"/></svg>
        (204) 555-0142
      </li>
      <li class="contact__email">
        <svg viewBox="0 0 14 14"><circle cx="7" cy="7" r="7" fill="var(--green)"/><rect x="3.5" y="4.5" width="7" height="5" fill="none" stroke="#1e1e1f" stroke-width="1.1"/><path d="M3.5 4.5 7 7.5l3.5-3" fill="none" stroke="#1e1e1f" stroke-width="1.1"/></svg>
        contact@corvantadental.ca
      </li>
      <li class="contact__address">420 MAPLECREST AVE, WINNIPEG, MB</li>
    </ul>
  </section>
</body>
</html>
```